Mezzanine Floor Manufacturer looking for a new business card design

We manufacture mezzanine floors and are providers of racking systems. We provide a range of items/services - simple rack repairs , full warehouse fit outs , manufacturer and install mezzanine floors , partitioning and large turnkey projects. Recently had a new website - www.corvane-shelving.co.uk and would like our business cards updating aswell . Our current card is single sided in the old logo colours (pdf attached) and needs updating.

Target Market(s)

We deal with large projects/ multi national companies and also smaller projects and companies throughout the UK ranging from a single warehouse to a large multi site company.

Industry/Entity Type

Business

Contact Information for Business Card

Will have job title,tel no's, email ,website address etc like example pdf

Requirements
Must have
• Hi - needs to use the colours of the logo & new website. Card needs to be professional

```html
<!DOCTYPE html>
<html lang="en">
<head>
<meta charset="utf-8">
<title>Corvane Shelving Ltd – Business Card</title>
<link rel="stylesheet" href="https://fonts.googleapis.com/css2?family=Open+Sans:wght@400;600;700&display=swap">
<style>
  :root {
    --brand-red: #d9213b;
    --brand-red-dark: #b5142b;
    --ink: #2b2b2b;
    --card: #ffffff;
    --card-shade: #f1f1f1;
    --backdrop: #e6e3de;
  }
  * { box-sizing: border-box; margin: 0; padding: 0; }
  html, body { width: 1200px; height: 780px; overflow: hidden; }
  body {
    background: var(--backdrop);
    font-family: "Open Sans", Arial, sans-serif;
    color: var(--ink);
    position: relative;
  }
  .card {
    position: absolute;
    width: 525px;
    height: 300px;
    background: linear-gradient(135deg, var(--card) 0%, var(--card-shade) 100%);
    box-shadow: 0 10px 28px rgba(0,0,0,.22);
    overflow: hidden;
  }
  .card--front { left: 50px; top: 70px; }
  .card--back  { left: 625px; top: 410px; }

  /* Front */
  .front-band { position: absolute; inset: 0; }
  .brand-mark {
    position: absolute; left: 28px; top: 148px;
    display: flex; align-items: center; gap: 10px;
  }
  .brand-mark__dot {
    width: 22px; height: 22px; border-radius: 50%;
    background: var(--brand-red);
  }
  .brand-mark__name {
    font-weight: 700; font-size: 30px; color: var(--brand-red);
  }
  .address {
    position: absolute; right: 28px; top: 18px;
    text-align: right; font-size: 12px; line-height: 1.45; font-style: normal;
  }
  .contact {
    position: absolute; left: 232px; top: 88px;
  }
  .contact__name {
    color: var(--brand-red); font-weight: 700; font-size: 21px;
    letter-spacing: .5px; text-transform: uppercase; line-height: 1.3;
  }
  .contact__role {
    font-size: 13px; text-transform: uppercase; margin-bottom: 6px;
  }
  .contact__list { list-style: none; font-size: 13.5px; line-height: 1.5; }
  .contact__list li { display: flex; align-items: center; gap: 7px; }
  .contact__icon {
    width: 13px; height: 13px; background: var(--brand-red);
    border-radius: 2px; display: inline-flex; align-items: center; justify-content: center;
  }
  .contact__icon svg { width: 9px; height: 9px; }

  /* Back */
  .company-name {
    position: absolute; left: 30px; top: 22px;
    color: var(--brand-red); font-weight: 700; font-size: 32px;
  }
  .services { position: absolute; left: 34px; top: 90px; color: var(--brand-red); }
  .services__title { font-weight: 700; font-size: 15px; margin-bottom: 6px; }
  .services__list { list-style: none; font-size: 13.5px; line-height: 1.6; }
  .services__list li { display: flex; align-items: center; gap: 10px; }
  .services__list li::before {
    content: ""; width: 8px; height: 8px; border-radius: 50%; background: var(--brand-red);
  }
  .web-address {
    position: absolute; left: 34px; bottom: 26px;
    color: var(--brand-red); font-size: 13px;
  }
  .social {
    position: absolute; right: 28px; bottom: 22px; display: flex; gap: 10px;
  }
  .social__tile {
    width: 30px; height: 30px; background: var(--brand-red); border-radius: 4px;
  }
</style>
</head>
<body>

<section class="card card--front" aria-label="Business card front">
  <svg class="front-band" viewBox="0 0 525 300" preserveAspectRatio="none" aria-hidden="true">
    <path d="M0 200 C 140 195, 220 255, 525 262 L525 300 L0 300 Z" fill="var(--brand-red)"/>
    <path d="M0 200 C 140 195, 220 255, 525 262" fill="none" stroke="var(--brand-red-dark)" stroke-width="3"/>
  </svg>
  <div class="brand-mark">
    <span class="brand-mark__dot"></span>
    <span class="brand-mark__name">Corvane</span>
  </div>
  <address class="address">
    12 Millstone Close<br>Harrowgate Business Park Ashby<br>Leicestershire LE6 4TR
  </address>
  <div class="contact">
    <h1 class="contact__name">Dean Whitfield</h1>
    <p class="contact__role">Technical Sales</p>
    <ul class="contact__list">
      <li><span class="contact__icon"><svg viewBox="0 0 10 10"><rect x="3" y="1" width="4" height="8" rx="1" fill="#fff"/></svg></span>07700 900412</li>
      <li><span class="contact__icon"><svg viewBox="0 0 10 10"><path d="M2 2 Q2 8 8 8 L8 6 L6 5.5 L5 6.5 Q3.5 5.5 3.5 5 L4.5 4 L4 2 Z" fill="#fff"/></svg></span>01632 960481</li>
      <li><span class="contact__icon"><svg viewBox="0 0 10 10"><rect x="1.5" y="3" width="7" height="5" fill="#fff"/><rect x="3" y="1" width="4" height="2.5" fill="#fff"/></svg></span>01632 960577</li>
      <li><span class="contact__icon"><svg viewBox="0 0 10 10"><rect x="1" y="2.5" width="8" height="5" fill="#fff"/><path d="M1 2.5 L5 5.5 L9 2.5" fill="none" stroke="var(--brand-red)" stroke-width="1"/></svg></span>sales@corvane-shelving.co.uk</li>
    </ul>
  </div>
</section>

<section class="card card--back" aria-label="Business card back">
  <h2 class="company-name">Corvane Shelving Ltd</h2>
  <div class="services">
    <h3 class="services__title">SERVICES</h3>
    <ul class="services__list">
      <li>simple rack repairs</li>
      <li>full warehouse fit outs</li>
      <li>manufacturer and install mezzanine floors</li>
      <li>partitioning and large turnkey projects</li>
    </ul>
  </div>
  <p class="web-address">www.corvane-shelving.co.uk</p>
  <div class="social" aria-label="Social media links">
    <span class="social__tile"></span>
    <span class="social__tile"></span>
    <span class="social__tile"></span>
    <span class="social__tile"></span>
  </div>
</section>

</body>
</html>
```